Service Proposal brochure

I have a list of services, references and details I can provide to create the service proposal from.

Target Market(s)

Project Managers in the Construction/Electrical Field Industry

Industry/Entity Type

Construction/Electrical Industry

Font styles to use
Serif

Colors
0054AA
0677BA
7BADD7
CADEEF
E8F1F8
FFF300
FFF600
FEFA6F
FFFEC7
FFFEE8

Requirements
Must have
• High vocabulary
Nice to have
• Creativity in the details of service work and layout of the brochure
Should not have
• So much wording that it becomes boring for the consumer

```html
<!DOCTYPE html>
<html lang="en">
<head>
<meta charset="utf-8">
<title>Service Proposal Brochure</title>
<link href="https://fonts.googleapis.com/css2?family=Noto+Serif:wght@400;700&family=Lato:wght@300;400&display=swap" rel="stylesheet">
<style>
:root{
  --blue:#0a62b0;
  --blue-deep:#0054AA;
  --yellow:#FFF300;
  --ink:#222;
  --grey-light:#f4f4f4;
  --grey-mid:#c2c3c4;
  --backdrop:#000;
}
*{margin:0;padding:0;box-sizing:border-box}
html,body{width:1200px;height:836px;overflow:hidden;background:var(--backdrop)}
body{position:relative;font-family:"Noto Serif",Georgia,serif;color:var(--ink)}
.page{position:absolute;top:90px;width:507px;height:655px;overflow:hidden}
.cover{left:78px;background:linear-gradient(180deg,#fff 0%,#f1f1f1 50%,var(--grey-mid) 100%)}
.services{left:615px;background:#fff}

.cover-photo{position:absolute;left:0;top:0;width:507px;height:320px;
  background:linear-gradient(180deg,#ececec 0%,#cfcfcf 40%,#e6e6e6 65%,rgba(255,255,255,0) 100%)}
.logo-tab{position:absolute;left:0;top:31px;width:183px;height:64px;background:#fff;
  clip-path:polygon(0 0,88% 0,100% 100%,0 100%)}
.logo-tab span{position:absolute;left:53px;top:14px;font-family:"Lato",Arial,sans-serif;font-weight:300;font-size:26px;letter-spacing:2px;color:#666}
.title{position:absolute;left:53px;top:220px;font-weight:700;color:var(--blue);font-size:43px;line-height:44px}

.ref{position:absolute;width:230px}
.ref .org{font-size:15.5px;line-height:17px;color:var(--blue)}
.ref .bar{width:95px;height:3px;background:var(--yellow);margin:8px 0 5px;clip-path:polygon(0 0,100% 0,97% 100%,0 100%)}
.ref .name{font-size:10.5px;color:var(--blue);line-height:12px;text-transform:uppercase}
.ref .role{font-size:7px;color:#333;line-height:9px}
.ref .contact{font-size:9px;line-height:12px;margin-top:4px;color:#222}

.band{position:absolute;left:0;width:507px}
.band-top{top:0;height:95px}
.band-bottom{bottom:0;height:40px}
.heading{position:absolute;left:54px;top:40px;font-size:19px;font-weight:700;color:#fff;letter-spacing:.3px}
.heading .accent{color:var(--yellow)}
.heading-rule{position:absolute;left:54px;top:63px;width:156px;height:3px;background:var(--yellow)}

.service{position:absolute;width:170px;text-align:center}
.service .badge{width:44px;height:44px;border-radius:50%;background:var(--blue);margin:0 auto;display:flex;align-items:center;justify-content:center}
.service .badge svg{width:26px;height:26px}
.service .label{margin-top:6px;font-size:10.3px;line-height:11.5px;color:#222}
.service .brands{font-size:8.3px;line-height:9.5px;color:#222}
</style>
</head>
<body>

<section class="page cover">
  <div class="cover-photo" role="img" aria-label="Monochrome city skyline and glass architecture photograph"></div>
  <div class="logo-tab"><span>LOGO</span></div>
  <h1 class="title">SERVICE<br>PROPOSAL</h1>

  <div class="ref" style="left:54px;top:350px">
    <div class="org">Redstone Valley University</div>
    <div class="bar"></div>
    <div class="name">Marcus Hale</div>
    <div class="role">Director of Campus Engineering</div>
    <div class="contact">Email: mhale@rvu.edu<br>Phone: 909-555-0142</div>
    <div class="bar" style="margin-top:7px"></div>
    <div class="name">Dennis Ward</div>
    <div class="role">Construction &amp; Wayfinding Senior Project Manager</div>
    <div class="contact">Email: dward@rvu.edu<br>Phone: (951)-555-0187</div>
  </div>

  <div class="ref" style="left:291px;top:350px">
    <div class="org">Pine Hollow Valley<br>Water District</div>
    <div class="bar"></div>
    <div class="name">Owen Pratt</div>
    <div class="role">Director of Operations</div>
    <div class="contact">Email: owen.pratt@phvwd.org<br>Phone: (951) 555-0163- ext.214</div>
  </div>

  <div class="ref" style="left:54px;top:521px">
    <div class="org">Cedar Ridge School District</div>
    <div class="bar"></div>
    <div class="name">Luis Moreno</div>
    <div class="role">Maintenance Supervisor</div>
    <div class="contact">Email: luis_moreno@crsd.us<br>Phone: (909) 555-0176</div>
  </div>

  <div class="ref" style="left:291px;top:521px">
    <div class="org">Halvorsen Engineering</div>
    <div class="bar"></div>
    <div class="name">Travis Kemp</div>
    <div class="role">Plant &amp; Facilities Maintenance Director</div>
  </div>
</section>

<section class="page services">
  <svg class="band band-top" viewBox="0 0 507 95" role="img" aria-label="Monochrome city skyline photograph band">
    <defs><linearGradient id="skyTop" x1="0" y1="0" x2="0" y2="1"><stop offset="0" stop-color="#9a9a9a"/><stop offset="1" stop-color="#6f6f6f"/></linearGradient></defs>
    <rect width="507" height="95" fill="url(#skyTop)"/>
    <path d="M0 84 C60 70 140 68 230 76 C320 84 420 90 507 86 L507 95 L0 95Z" fill="#fff"/>
  </svg>
  <div class="heading"><span class="accent">SERVICE'S</span> INCLUDE:</div>
  <div class="heading-rule"></div>

  <svg class="band band-bottom" viewBox="0 0 507 40" role="img" aria-label="Monochrome city skyline photograph band">
    <rect width="507" height="40" fill="#8a8a8a"/>
    <path d="M0 0 L507 0 L507 10 C420 4 330 2 250 8 C160 14 80 4 0 8Z" fill="#fff"/>
  </svg>

  <div class="service" style="left:15px;top:100px">
    <div class="badge"><svg viewBox="0 0 24 24"><path d="M14 2 L5 14 H11 L9 22 L19 9 H13Z" fill="var(--yellow)"/></svg></div>
    <div class="label">POWER<div class="brands">Upgrade/ Additional</div></div>
  </div>
  <div class="service" style="left:165px;top:100px">
    <div class="badge"><svg viewBox="0 0 24 24" fill="none" stroke="var(--yellow)" stroke-width="1.6"><rect x="4" y="4" width="6" height="14" rx="1"/><rect x="13" y="7" width="7" height="11" rx="1"/><path d="M4 21 H20"/></svg></div>
    <div class="label">NEW EQUIPMENT</div>
  </div>
  <div class="service" style="left:324px;top:100px">
    <div class="badge"><svg viewBox="0 0 24 24"><circle cx="8" cy="9" r="3" fill="var(--yellow)"/><path d="M3 19 C3 14 13 14 13 19Z" fill="var(--yellow)"/><circle cx="17" cy="7" r="4" fill="none" stroke="var(--yellow)" stroke-width="1.6"/><path d="M15 7 L16.5 8.5 L19 5.5" fill="none" stroke="var(--yellow)" stroke-width="1.6"/></svg></div>
    <div class="label">Title 24<br>commissioning and<br>acceptance</div>
  </div>

  <div class="service" style="left:15px;top:185px">
    <div class="badge"><svg viewBox="0 0 24 24"><circle cx="12" cy="11" r="5" fill="var(--yellow)"/><rect x="10" y="16" width="4" height="4" fill="var(--yellow)"/><path d="M12 2 V4 M4 11 H6 M18 11 H20 M6 5 L7.5 6.5 M18 5 L16.5 6.5" stroke="var(--yellow)" stroke-width="1.4"/></svg></div>
    <div class="label">LIGHTING<div class="brands">Upgrade/ additional/ retrofits</div></div>
  </div>
  <div class="service" style="left:165px;top:185px">
    <div class="badge"><svg viewBox="0 0 24 24"><rect x="3" y="7" width="16" height="10" rx="1" fill="none" stroke="var(--yellow)" stroke-width="1.8"/><rect x="19" y="10" width="2" height="4" fill="var(--yellow)"/><rect x="5.5" y="9.5" width="3" height="5" fill="var(--yellow)"/><rect x="9.5" y="9.5" width="3" height="5" fill="var(--yellow)"/><rect x="13.5" y="9.5" width="3" height="5" fill="var(--yellow)"/></svg></div>
    <div class="label">VOLQUERRA BATTERY<br>PACKS</div>
  </div>
  <div class="service" style="left:324px;top:185px">
    <div class="badge"><svg viewBox="0 0 24 24"><circle cx="10" cy="10" r="6" fill="var(--yellow)"/><circle cx="10" cy="10" r="2.2" fill="var(--blue)"/><path d="M14 15 L18 20 M16 12 H20" stroke="var(--yellow)" stroke-width="2"/></svg></div>
    <div class="label">FIRE ALARM<div class="brands">Kestrane, Tarnvik,<br>Flarith</div></div>
  </div>

  <div class="service" style="left:15px;top:269px">
    <div class="badge"><svg viewBox="0 0 24 24"><path d="M12 3 L21 11 H18 V20 H6 V11 H3Z" fill="var(--yellow)"/><path d="M10 17 L14 12" stroke="var(--blue)" stroke-width="1.8"/></svg></div>
    <div class="label">REMODELS</div>
  </div>
  <div class="service" style="left:165px;top:269px">
    <div class="badge"><svg viewBox="0 0 24 24"><rect x="3" y="6" width="18" height="12" rx="2" fill="var(--yellow)"/><path d="M13 8 L9 13 H12 L11 16 L15 11 H12Z" fill="var(--blue)"/></svg></div>
    <div class="label">GENERATORS AND<br>AUTOMATIC TRANSFER<br>SWITCHES</div>
  </div>
  <div class="service" style="left:324px;top:269px">
    <div class="badge"><svg viewBox="0 0 24 24"><path d="M12 2 L20 5 V11 C20 16 16 20 12 22 C8 20 4 16 4 11 V5Z" fill="var(--yellow)"/><circle cx="12" cy="10" r="2.3" fill="var(--blue)"/><rect x="11" y="11" width="2" height="5" fill="var(--blue)"/></svg></div>
    <div class="label">SECURITY<br>(INTRUSION)<div class="brands">Tarnvik, Qestral, Harlowe,<br>Alarmity</div></div>
  </div>

  <div class="service" style="left:15px;top:364px">
    <div class="badge"><svg viewBox="0 0 24 24" fill="none" stroke="var(--yellow)" stroke-width="1.6"><circle cx="12" cy="4" r="1.6"/><path d="M11 5.5 L6 20 M13 5.5 L18 20 M3 21 H21 M8 15 H16"/></svg></div>
    <div class="label">DESIGN BUILD &amp;<br>DESIGN ASSIST</div>
  </div>
  <div class="service" style="left:165px;top:364px">
    <div class="badge"><svg viewBox="0 0 24 24"><circle cx="6" cy="6" r="2" fill="var(--yellow)"/><rect x="4" y="9" width="4" height="11" rx="1" fill="var(--yellow)"/><circle cx="18" cy="6" r="2" fill="var(--yellow)"/><rect x="16" y="9" width="4" height="11" rx="1" fill="var(--yellow)"/><path d="M9 12 H15" stroke="var(--yellow)" stroke-width="1.2" stroke-dasharray="1.5 1.5"/></svg></div>
    <div class="label">PREVENTIVE<br>Maintenance and Testing<br>(ETCA 2 Certified)</div>
  </div>
  <div class="service" style="left:324px;top:364px">
    <div class="badge"><svg viewBox="0 0 24 24" fill="none" stroke="var(--yellow)" stroke-width="1.4"><circle cx="12" cy="12" r="8"/><circle cx="12" cy="12" r="5"/><circle cx="12" cy="12" r="2"/><path d="M16 7 L17.5 8.5 L20 5.5" stroke-width="1.8"/></svg></div>
    <div class="label">SECURITY<br>(ACCESS CONTROL)<div class="brands">Lockrane &amp; Ordivo</div></div>
  </div>

  <div class="service" style="left:15px;top:455px">
    <div class="badge"><svg viewBox="0 0 24 24"><path d="M10 2 H15 L13 10 H17 L11 22 L12 13 H8Z" fill="var(--yellow)"/></svg></div>
    <div class="label">MEDIUM<br>VOLTAGE</div>
  </div>
  <div class="service" style="left:165px;top:455px">
    <div class="badge"><svg viewBox="0 0 24 24"><rect x="10" y="2" width="4" height="20" rx="1" fill="var(--yellow)"/><path d="M4 9 H9 M15 15 H20" stroke="var(--yellow)" stroke-width="1.8"/></svg></div>
    <div class="label">ARCH FLASH/<br>Coordination Study</div>
  </div>
  <div class="service" style="left:324px;top:455px">
    <div class="badge"><svg viewBox="0 0 24 24"><path d="M6 7 L19 4 L20 10 L8 13Z" fill="var(--yellow)"/><rect x="6" y="13" width="2.5" height="5" fill="var(--yellow)"/><rect x="4" y="17" width="6" height="2" fill="var(--yellow)"/></svg></div>
    <div class="label">SECURITY<br>(CAMERAS)<div class="brands">Quorvix, Lumistra, Tarnvik</div></div>
  </div>

  <div class="service" style="left:79px;top:540px">
    <div class="badge"><svg viewBox="0 0 24 24"><path d="M4 5 H18 L21 8.5 L18 12 H4Z" fill="var(--yellow)"/><rect x="10" y="12" width="3" height="10" fill="var(--yellow)"/></svg></div>
    <div class="label">PUBLIC ADDRESS<br>Sonarith &amp; Vellacor</div>
  </div>
  <div class="service" style="left:234px;top:540px">
    <div class="badge"><svg viewBox="0 0 24 24" fill="none" stroke="var(--yellow)" stroke-width="1.4"><rect x="4" y="6" width="16" height="12"/><path d="M7 6 V18 M10 6 V18 M13 6 V18 M16 6 V18 M2 12 H4 M20 12 H22"/></svg></div>
    <div class="label">STRUCTURED CABLE<br>Corvance, Strandley</div>
  </div>
</section>

</body>
</html>
```